Maple Ridge business card design

Card needs to include the following text/items:
Company Logo
Tobin Marsh
Phone # - 555-318-7642
service@mapleridgelandscaping.example
Lawn & landscape maintenance services

```html
<!DOCTYPE html>
<html lang="en">
<head>
<meta charset="utf-8">
<title>Maple Ridge business card</title>
<link rel="stylesheet" href="https://fonts.googleapis.com/css2?family=Roboto+Condensed:wght@400;700&display=swap">
<style>
  :root {
    --page-bg: #e6e7e9;
    --card-bg: #ffffff;
    --green-deep: #0f4a24;
    --green-band-dark: #1b6e35;
    --green-band-light: #5b9142;
    --mark-fill: #2f7a3b;
  }
  * { margin: 0; padding: 0; box-sizing: border-box; }
  html, body {
    width: 1200px;
    height: 1006px;
    overflow: hidden;
    background: var(--page-bg);
    font-family: "Roboto Condensed", Arial, sans-serif;
    color: var(--green-deep);
  }
  .card {
    position: absolute;
    top: 148px;
    width: 405px;
    height: 709px;
    background: var(--card-bg);
    overflow: hidden;
  }
  .card--front { left: 133px; }
  .card--back { left: 639px; }
  .card__bands { position: absolute; inset: 0; }
  .brand {
    position: absolute;
    left: 0;
    width: 100%;
    text-align: center;
  }
  .brand__mark {
    display: block;
    margin: 0 auto;
    border-radius: 50%;
    background: var(--mark-fill);
  }
  .brand__name {
    display: block;
    font-weight: 700;
    color: var(--green-deep);
    white-space: nowrap;
  }
  .card--front .brand { top: 118px; }
  .card--front .brand__mark { width: 110px; height: 110px; }
  .card--front .brand__name { font-size: 34px; margin-top: 12px; }
  .card--back .brand { top: 238px; }
  .card--back .brand__mark { width: 170px; height: 170px; }
  .card--back .brand__name { font-size: 50px; margin-top: 16px; }
  .holder {
    position: absolute;
    top: 340px;
    width: 100%;
    text-align: center;
    font-size: 44px;
    font-weight: 700;
    letter-spacing: -0.3px;
  }
  .tagline {
    position: absolute;
    top: 415px;
    width: 100%;
    text-align: center;
    font-size: 25px;
    line-height: 26px;
    font-weight: 400;
  }
  .contact {
    position: absolute;
    width: 100%;
    display: flex;
    justify-content: center;
    align-items: center;
    gap: 5px;
    font-size: 20px;
    font-weight: 400;
  }
  .contact--phone { top: 511px; }
  .contact--email { top: 542px; }
  .contact__icon { width: 20px; height: 20px; flex: none; }
</style>
</head>
<body>

<section class="card card--front">
  <svg class="card__bands" width="405" height="709" viewBox="0 0 405 709" aria-hidden="true">
    <defs>
      <linearGradient id="band-top" x1="0" y1="0" x2="1" y2="0">
        <stop offset="0" stop-color="var(--green-band-dark)"/>
        <stop offset="1" stop-color="var(--green-band-light)"/>
      </linearGradient>
      <linearGradient id="band-bottom" x1="0" y1="0" x2="1" y2="0">
        <stop offset="0" stop-color="var(--green-band-light)"/>
        <stop offset="1" stop-color="var(--green-band-dark)"/>
      </linearGradient>
    </defs>
    <path d="M0 0 H405 V30 C300 22 110 20 0 86 Z" fill="url(#band-top)"/>
    <path d="M0 678 C140 688 320 670 405 619 V709 H0 Z" fill="url(#band-bottom)"/>
  </svg>

  <div class="brand">
    <span class="brand__mark" aria-hidden="true"></span>
    <span class="brand__name">Maple Ridge</span>
  </div>

  <h1 class="holder">Tobin Marsh</h1>
  <p class="tagline">Lawn &amp; landscape<br>maintenance services</p>

  <p class="contact contact--phone">
    <svg class="contact__icon" viewBox="0 0 24 24" aria-hidden="true">
      <path fill="var(--green-deep)" d="M6.6 10.8a15.1 15.1 0 0 0 6.6 6.6l2.2-2.2c.3-.3.7-.4 1-.2 1.1.4 2.3.6 3.6.6.6 0 1 .4 1 1V20c0 .6-.4 1-1 1C10.6 21 3 13.4 3 4c0-.6.4-1 1-1h3.5c.6 0 1 .4 1 1 0 1.3.2 2.5.6 3.6.1.3 0 .7-.2 1z"/>
    </svg>
    <span>555-318-7642</span>
  </p>
  <p class="contact contact--email">
    <svg class="contact__icon" viewBox="0 0 24 24" aria-hidden="true">
      <rect x="2" y="5" width="20" height="14" fill="none" stroke="var(--green-deep)" stroke-width="1.8"/>
      <path d="M2 5l10 8 10-8M2 19l7-7M22 19l-7-7" fill="none" stroke="var(--green-deep)" stroke-width="1.6"/>
    </svg>
    <span>service@mapleridgelandscaping.example</span>
  </p>
</section>

<section class="card card--back">
  <div class="brand">
    <span class="brand__mark" aria-hidden="true"></span>
    <span class="brand__name">Maple Ridge</span>
  </div>
</section>

</body>
</html>
```